Label to go onto food packaging.

We need to create a visually interesting and appealing label to stick onto our take away food packaging. The label should contain information of the food products our cafe sells. The label is to go onto biodegradable food bowls and clam shell packaging.
The information is basically the lines we sell - buddha bowls, super smoothies, vegan burgers and curries. And also the slogan 'nourish and refresh'. We have a logo design that we would like to incorporate onto the label (but not essential)
The design will go onto a rectangle strip label.
The colours of our food outlet are splashes of yellow, blue and grey in a white interior.
We also feature a large garden green wall. You may view images from our instagram page bright pebble kitchen

Target Market(s)

Young professional, health conscious, plant based eaters. To be used on takeaway packaging.

Industry/Entity Type

Food Production

Font styles to use
Sans Serif

Colors

Designer to choose colors to be used in the design.

Requirements
Must have
• Bold, appealing, informative.
Nice to have
• Logo incorporated, possibly as a watermark?
Should not have
• No floral shapes. If incorporating the logo, use a circle or nothing around it. No pictures/photos of food

```html
<!DOCTYPE html>
<html lang="en">
<head>
<meta charset="utf-8">
<title>Bright Pebble Kitchen – Packaging Label</title>
<link rel="stylesheet" href="https://fonts.googleapis.com/css2?family=Lilita+One&display=swap">
<style>
  :root {
    --sky-blue: #0795db;
    --sun-yellow: #fff212;
  }
  html, body {
    margin: 0;
    padding: 0;
    width: 1200px;
    height: 320px;
    overflow: hidden;
    background: var(--sky-blue);
  }
  .label {
    position: relative;
    width: 1200px;
    height: 320px;
    background: var(--sky-blue);
  }
  .label-panel {
    position: absolute;
    left: 20px;
    top: 20px;
    width: 1160px;
    height: 280px;
    border-radius: 42px;
    background: var(--sun-yellow);
  }
  .product-list {
    margin: 0;
    padding: 0;
    list-style: none;
  }
  .pill {
    position: absolute;
    display: flex;
    align-items: center;
    justify-content: center;
    margin: 0;
    background: var(--sky-blue);
    border-radius: 20px;
    font-family: "Lilita One", sans-serif;
    font-weight: 400;
    color: var(--sky-blue);
    -webkit-text-stroke: 4px var(--sun-yellow);
    paint-order: stroke fill;
    letter-spacing: 1px;
    white-space: nowrap;
  }
  .slogan {
    left: 332px;
    top: 36px;
    width: 536px;
    height: 80px;
    font-size: 52px;
  }
  .product {
    width: 360px;
    font-size: 36px;
  }
  .product--buddha-bowls    { left: 78px;  top: 144px; height: 60px; }
  .product--super-smoothies { left: 78px;  top: 228px; height: 58px; }
  .product--vegan-burgers   { left: 762px; top: 139px; height: 59px; }
  .product--curries         { left: 762px; top: 221px; height: 59px; }
  .brand {
    position: absolute;
    left: 440px;
    top: 195px;
    width: 320px;
    margin: 0;
    text-align: center;
    font-family: "Lilita One", sans-serif;
    font-weight: 400;
    font-size: 26px;
    line-height: 30px;
    color: var(--sky-blue);
    white-space: nowrap;
  }
</style>
</head>
<body>
  <main class="label">
    <div class="label-panel"></div>
    <h1 class="pill slogan">Nourish &amp; Refresh</h1>
    <ul class="product-list">
      <li class="pill product product--buddha-bowls">Buddha Bowls</li>
      <li class="pill product product--super-smoothies">Super Smoothies</li>
      <li class="pill product product--vegan-burgers">Vegan Burgers</li>
      <li class="pill product product--curries">Curries</li>
    </ul>
    <p class="brand">Bright Pebble Kitchen</p>
  </main>
</body>
</html>
```